V Glowing Business Cards
Salon & Spa
Project: V Glowing Business Cards
V Glowing Business Cards - Salon & Spa
Creative Brief
Professional
Maribel Trostle
Owner
4100 Route 27 East Denville, NJ 07834
mtrostle@vglowingstudio.example
www.VGlowingstudio.example
we are looking for an elegant look and feel that is enticing and appealing for women of all ages (18-80 )

```html
<!DOCTYPE html>
<html lang="en">
<head>
<meta charset="utf-8">
<title>V Glowing Business Cards</title>
<link rel="stylesheet" href="https://fonts.googleapis.com/css2?family=Cinzel:wght@400;600&display=swap">
<style>
  :root {
    --backdrop: #e6e6e6;
    --ink: #111111;
    --card-black: #0b0b0b;
    --card-white: #f4f4f4;
    --silver: #c9c9c9;
    --muted: #3a3a3a;
    --paper-text: #ffffff;
  }
  * { margin: 0; padding: 0; box-sizing: border-box; }
  html, body {
    width: 1200px; height: 901px; overflow: hidden;
    background: var(--backdrop);
    font-family: "Cinzel", serif;
  }
  .canvas { position: relative; width: 1200px; height: 901px; }
  .card {
    position: absolute; top: 296px;
    width: 540px; height: 309px;
    border-radius: 18px; overflow: hidden;
    box-shadow: 0 10px 28px rgba(0,0,0,0.22);
  }
  .card-front { left: 40px; background: var(--card-black); }
  .card-back {
    left: 620px;
    background: linear-gradient(135deg, #fbfbfb 0%, var(--card-white) 55%, #dcdcdc 100%);
  }

  .brand-name {
    font-family: "Cinzel", serif;
    font-weight: 400;
    letter-spacing: 2px;
    white-space: nowrap;
  }
  .card-front .brand-name {
    position: absolute; left: 0; right: 0; top: 128px;
    text-align: center; font-size: 44px; color: var(--silver);
  }
  .card-back .brand-name {
    position: absolute; left: 28px; top: 78px;
    font-size: 34px; color: var(--ink);
  }

  .contact {
    position: absolute; left: 300px; top: 70px;
    color: var(--ink);
  }
  .contact-name { font-size: 15px; font-weight: 600; letter-spacing: 0.5px; }
  .contact-role { font-size: 10px; color: var(--muted); margin-top: 2px; }
  .contact-address { font-size: 10.5px; line-height: 1.45; margin-top: 18px; }
  .contact-line {
    display: flex; align-items: center; gap: 8px;
    font-size: 10px; margin-top: 6px; white-space: nowrap;
  }
  .contact-line:first-of-type { margin-top: 14px; }
  .contact-line svg { width: 12px; height: 12px; flex: none; }

  .swoosh { position: absolute; left: 0; bottom: 0; width: 540px; height: 140px; }
  .website {
    position: absolute; left: 36px; bottom: 18px;
    font-size: 12px; letter-spacing: 1px; color: var(--paper-text);
    white-space: nowrap;
  }
</style>
</head>
<body>
<main class="canvas">
  <section class="card card-front" aria-label="Card front">
    <div class="brand-name">V Glowing</div>
  </section>

  <section class="card card-back" aria-label="Card back">
    <div class="brand-name">V Glowing</div>

    <div class="contact">
      <div class="contact-name">Maribel Trostle</div>
      <div class="contact-role">Owner</div>
      <div class="contact-address">4100 Route 27 East<br>Brookmere, NJ 07990</div>
      <div class="contact-line">
        <svg viewBox="0 0 12 12" aria-hidden="true"><path d="M2.5 1h2l1 2.5-1.3 1a6 6 0 0 0 3.3 3.3l1-1.3 2.5 1v2c0 .8-.7 1.5-1.5 1.5A9.5 9.5 0 0 1 1 2.5C1 1.7 1.7 1 2.5 1z" fill="var(--ink)"/></svg>
        <span>973-555-0142</span>
      </div>
      <div class="contact-line">
        <svg viewBox="0 0 12 12" aria-hidden="true"><rect x="1" y="2.5" width="10" height="7" fill="none" stroke="var(--ink)" stroke-width="1"/><path d="M1 2.5l5 4 5-4" fill="none" stroke="var(--ink)" stroke-width="1"/></svg>
        <span>mtrostle@vglowingstudio.example</span>
      </div>
    </div>

    <svg class="swoosh" viewBox="0 0 540 140" preserveAspectRatio="none" aria-hidden="true">
      <path d="M0 28 C150 84 330 90 540 56 L540 140 L0 140 Z" fill="var(--card-black)"/>
      <path d="M0 38 C150 92 330 96 540 66" fill="none" stroke="var(--paper-text)" stroke-width="2.5"/>
      <path d="M160 24 C300 80 430 80 540 60 L540 76 C420 96 300 92 160 24 Z" fill="var(--card-black)" opacity="0.9"/>
    </svg>
    <div class="website">www.VGlowingstudio.example</div>
  </section>
</main>
</body>
</html>
```